Business Card design for shipping company 'FERNHOLT INTERNATIONAL LTD'

Classic / traditional business card in black Garamond / Times New Roman or similar text for a shipping / marine transport company, containing the following information:

QUOTE

FERNHOLT INTERNATIONAL LTD

MARTIN QUESTEDGE FICS

T: +44 7902 615370
E: cargo@fernholt-example.com

UNQUOTE

Target Market(s)

Marine / Shipping industry

Contact Information for Business Card

FERNHOLT INTERNATIONAL LTD MARTIN QUESTEDGE FICS T: +44 7902 615370 E: cargo@fernholt-example.com

Font styles to use
Serif

Colors

Designer to choose colors to be used in the design.

Requirements
Must have
• Garamond / Times New Roman or similar text in black colour

```html
<!DOCTYPE html>
<html lang="en">
<head>
<meta charset="utf-8">
<title>Fernholt International Ltd – Business Card</title>
<link rel="stylesheet" href="https://fonts.googleapis.com/css2?family=Tinos:wght@400;700&display=swap">
<style>
  :root {
    --backdrop: #e6e3df;
    --card: #0f0f0f;
    --card-sheen: #1c1c1c;
    --ink: #ffffff;
    --shadow: rgba(0, 0, 0, 0.28);
  }
  * { box-sizing: border-box; margin: 0; padding: 0; }
  html, body {
    width: 1200px;
    height: 886px;
    overflow: hidden;
    background: var(--backdrop);
  }
  .canvas {
    width: 1200px;
    height: 886px;
    display: flex;
    flex-direction: column;
    align-items: center;
    justify-content: center;
    gap: 44px;
  }
  .card {
    position: relative;
    width: 660px;
    height: 377px;
    border-radius: 26px;
    background: linear-gradient(115deg, var(--card) 0%, var(--card) 38%, var(--card-sheen) 55%, var(--card) 75%);
    box-shadow: 0 10px 28px var(--shadow);
    color: var(--ink);
    font-family: "Tinos", "Times New Roman", serif;
  }
  .card--front {
    display: flex;
    align-items: center;
    justify-content: center;
  }
  .front-name {
    font-weight: 700;
    font-size: 24px;
    letter-spacing: 0.06em;
  }
  .back-company {
    position: absolute;
    left: 56px;
    top: 118px;
    font-weight: 700;
    font-size: 31px;
    line-height: 1.08;
    letter-spacing: 0.05em;
  }
  .contact {
    position: absolute;
    right: 48px;
    bottom: 62px;
    font-size: 17px;
    line-height: 1.35;
  }
  .contact-name {
    font-size: 20px;
    letter-spacing: 0.03em;
    margin-bottom: 4px;
  }
  .contact-line {
    display: flex;
    align-items: center;
    gap: 10px;
    padding-left: 40px;
  }
  .contact-line svg {
    width: 16px;
    height: 14px;
    fill: var(--ink);
    flex: none;
  }
</style>
</head>
<body>
<main class="canvas">
  <section class="card card--front" aria-label="Card front">
    <h1 class="front-name">FERNHOLT INTERNATIONAL LTD</h1>
  </section>

  <section class="card card--back" aria-label="Card back">
    <h2 class="back-company">FERNHOLT<br>INTERNATIONAL<br>LTD</h2>
    <div class="contact">
      <p class="contact-name">MARTIN QUESTEDGE FICS</p>
      <p class="contact-line">
        <svg viewBox="0 0 16 14" aria-hidden="true">
          <path d="M1 4.5C1 2.5 4 1 8 1s7 1.5 7 3.5v1h-3.5V4H4.5v1.5H1z"/>
          <path d="M3.5 6.5h9L14.5 13h-13z"/>
        </svg>
        <span>+44 7902 615370</span>
      </p>
      <p class="contact-line">
        <svg viewBox="0 0 16 14" aria-hidden="true">
          <path d="M1 2h14v10H1z M2.5 3.2 8 7.6l5.5-4.4z" fill-rule="evenodd"/>
        </svg>
        <span>cargo@fernholt-example.com</span>
      </p>
    </div>
  </section>
</main>
</body>
</html>
```